Stationary & Business Card for Talvo Co, LLC
Talvo Co, LLC
Professional
Adrian Pellworth, MD
President
2918 Larkfield Ave., Suite C-240
Bethesda, MD 20846
dradrian@talvocollc.com
www.talvocollc.com
Our tagline is Your Partner in Personalized Healthcare.
We would like a solid color for our back - either matching the purple or gold of our logo

```html
<!DOCTYPE html>
<html lang="en">
<head>
<meta charset="utf-8">
<title>Talvo Co, LLC — Business Card</title>
<link rel="stylesheet" href="https://fonts.googleapis.com/css2?family=Open+Sans:ital,wght@0,400;0,600;1,400&display=swap">
<style>
  :root {
    --purple: #4b2366;
    --gold: #d4a92c;
    --ink: #5a4a66;
    --paper: #ffffff;
    --backdrop: #d9d9db;
  }
  * { box-sizing: border-box; margin: 0; padding: 0; }
  html, body { width: 1200px; height: 895px; overflow: hidden; }
  body {
    background: var(--backdrop);
    font-family: "Open Sans", Arial, sans-serif;
    display: flex;
    flex-direction: column;
    align-items: center;
    justify-content: center;
    gap: 40px;
  }
  .card {
    width: 680px;
    height: 388px;
    background: var(--paper);
    position: relative;
  }
  .card--front { border: 14px solid var(--purple); }
  .card--back { border: 14px solid var(--gold); }

  /* front */
  .brand {
    position: absolute;
    left: 44px;
    top: 56px;
    display: flex;
    align-items: center;
    gap: 18px;
  }
  .brand-dot {
    width: 82px; height: 82px;
    border-radius: 50%;
    background: var(--purple);
  }
  .brand-divider {
    width: 2px; height: 92px;
    background: var(--gold);
  }
  .brand-name {
    color: var(--purple);
    font-weight: 600;
    font-size: 46px;
    line-height: 1;
    letter-spacing: 0.5px;
  }
  .brand-tagline {
    margin-top: 8px;
    color: var(--purple);
    font-size: 9.5px;
    letter-spacing: 1.6px;
    text-transform: uppercase;
  }
  .person {
    position: absolute;
    left: 44px;
    top: 196px;
    width: 250px;
    text-align: right;
    color: var(--ink);
    font-size: 13px;
    line-height: 1.45;
  }
  .person-name { color: var(--purple); font-style: italic; font-size: 16px; }
  .person-title { font-style: italic; margin-bottom: 6px; }
  .contact {
    position: absolute;
    left: 330px;
    top: 196px;
    list-style: none;
    color: var(--ink);
    font-size: 13px;
  }
  .contact li {
    display: flex;
    align-items: center;
    gap: 10px;
    height: 24px;
  }
  .contact svg { width: 16px; height: 16px; flex: none; }

  /* back */
  .back-mark {
    position: absolute;
    left: 60px;
    top: 54px;
    display: flex;
    align-items: center;
    gap: 22px;
  }
  .back-dot {
    width: 150px; height: 150px;
    border-radius: 50%;
    background: var(--purple);
  }
  .back-name {
    color: var(--purple);
    font-weight: 600;
    font-size: 40px;
  }
  .back-web {
    position: absolute;
    right: 46px;
    bottom: 56px;
    color: var(--ink);
    font-size: 19px;
    letter-spacing: 4px;
  }
</style>
</head>
<body>

  <section class="card card--front" aria-label="Business card front">
    <div class="brand">
      <div class="brand-dot"></div>
      <div class="brand-divider"></div>
      <div class="brand-text">
        <div class="brand-name">Talvo Co, LLC</div>
        <div class="brand-tagline">Your Partner in Personalized Healthcare</div>
      </div>
    </div>

    <div class="person">
      <div class="person-name">Adrian Pellworth, MD</div>
      <div class="person-title">President</div>
      <div>2918 Larkfield Ave., Suite C-240</div>
      <div>Bethesda, MD 20846</div>
    </div>

    <ul class="contact">
      <li>
        <svg viewBox="0 0 16 16"><circle cx="8" cy="8" r="8" fill="var(--purple)"/><path d="M5.5 4.5l1.4 1.6-.8 1c.5 1 1.3 1.8 2.3 2.3l1-.8 1.6 1.4-.7 1.3c-2.8-.4-5-2.6-5.4-5.4z" fill="#fff"/></svg>
        (240) 555-0148
      </li>
      <li>
        <svg viewBox="0 0 16 16"><circle cx="8" cy="8" r="8" fill="var(--purple)"/><rect x="4.5" y="5" width="7" height="6" rx="1" fill="#fff"/></svg>
        (240) 555-0162
      </li>
      <li>
        <svg viewBox="0 0 16 16"><circle cx="8" cy="8" r="8" fill="var(--purple)"/><rect x="4" y="5" width="8" height="6" fill="#fff"/><path d="M4 5l4 3.2L12 5" stroke="var(--purple)" fill="none"/></svg>
        dradrian@talvocollc.com
      </li>
      <li>
        <svg viewBox="0 0 16 16"><circle cx="8" cy="8" r="8" fill="var(--purple)"/><circle cx="8" cy="8" r="4" fill="none" stroke="#fff"/><path d="M4 8h8M8 4v8" stroke="#fff"/></svg>
        www.talvocollc.com
      </li>
    </ul>
  </section>

  <section class="card card--back" aria-label="Business card back">
    <div class="back-mark">
      <div class="back-dot"></div>
      <div class="back-name">Talvo Co, LLC</div>
    </div>
    <div class="back-web">www.talvocollc.com</div>
  </section>

</body>
</html>
```